practice letterhead

I need a letterhead design for a new company that is a veterinary specialty company. I am conservative. I want it to look professional - not "cutesy"

I need my name, credentials, address, phone number and website/email on it.

My personal information is as follows: Marisol Tedder, DVM, DACVIM (Neurology) Certified Veterinary Pain Practitioner (or CVPP) Certified Canine Rehabilitation Therapist (or CCRT) 4170 Larkfield Hwy Elmsbury, NH 03299 508-347-6620 marisol.tedder@petspineandcare.com www.petspineandcare.com

```html
<!DOCTYPE html>
<html lang="en">
<head>
<meta charset="utf-8">
<title>Pet Spine and Care Center – Stationery</title>
<link href="https://fonts.googleapis.com/css2?family=Arimo:wght@700&family=Questrial&display=swap" rel="stylesheet">
<style>
  :root {
    --backdrop: #7b7b7b;
    --paper: #f7f7f7;
    --paper-shade: #ececec;
    --navy: #17323f;
    --sage: #6f9a8a;
    --ink: #4a4f52;
    --band-text: #c9d6d2;
  }
  * { box-sizing: border-box; margin: 0; padding: 0; }
  html, body { width: 1200px; height: 800px; overflow: hidden; }
  body { background: var(--backdrop); position: relative; font-family: "Questrial", sans-serif; }

  .sheet { position: absolute; background: var(--paper); overflow: hidden; }

  /* Envelope back, flap open */
  .envelope-back { left: 70px; top: 60px; width: 410px; height: 340px; border-radius: 8px 8px 0 0; }
  .envelope-back .flap-lining { position: absolute; left: 0; top: 0; width: 100%; height: 150px;
    background: linear-gradient(180deg, #e6e7e7, #dcdede); }
  .envelope-back .pocket { position: absolute; left: 0; top: 0; width: 100%; height: 340px; }

  /* Envelope front */
  .envelope-front { left: 85px; top: 422px; width: 405px; height: 300px; border-radius: 8px 8px 0 0; }
  .envelope-front .flap { position: absolute; left: 0; top: 0; width: 100%; height: 88px; background: var(--navy); }
  .envelope-front .flap-mark { position: absolute; left: 195px; top: 32px; width: 16px; height: 16px;
    border-radius: 50%; background: var(--sage); }
  .envelope-front .brand { position: absolute; left: 32px; top: 108px; }
  .envelope-front .return-address { position: absolute; left: 108px; top: 282px; font-size: 6px; color: var(--band-text); }
  .envelope-front .footer-curve { position: absolute; left: 0; bottom: 0; }

  .brand { display: flex; align-items: center; gap: 6px; }
  .brand-dot { width: 14px; height: 14px; border-radius: 50%; background: var(--navy); flex: none; }
  .brand-name { font-family: "Arimo", sans-serif; font-weight: 700; color: var(--sage); font-size: 13px; line-height: 1.1; }

  /* Letterhead */
  .letterhead { left: 628px; top: 85px; width: 464px; height: 650px; }
  .letterhead .contact { position: absolute; left: 94px; top: 42px; font-size: 6.5px; color: var(--ink); line-height: 1.45; }
  .contact-row { display: flex; align-items: center; gap: 4px; }
  .contact-row .icon { width: 6px; height: 6px; }
  .letterhead .brand { position: absolute; right: 18px; top: 68px; }
  .letterhead .brand-name { font-size: 14px; }
  .letterhead .fold { position: absolute; left: 0; width: 100%; height: 1px; background: var(--paper-shade); }
  .letterhead .footer-curve { position: absolute; left: 0; bottom: 0; }
  .letterhead .credentials { position: absolute; left: 32px; bottom: 16px; font-size: 6px; color: var(--band-text); white-space: nowrap; }
  .credentials strong { color: var(--sage); font-weight: 400; letter-spacing: .4px; }
</style>
</head>
<body>

<section class="sheet envelope-back" aria-label="Envelope back">
  <div class="flap-lining" role="img" aria-label="Envelope lining with repeating light grey brand pattern"></div>
  <svg class="pocket" width="410" height="340" viewBox="0 0 410 340">
    <path d="M0 140 L40 100 L370 100 L410 140 L410 340 L0 340 Z" fill="var(--paper)"/>
  </svg>
</section>

<section class="sheet envelope-front" aria-label="Envelope front">
  <div class="flap"></div>
  <span class="flap-mark"></span>
  <div class="brand">
    <span class="brand-dot"></span>
    <span class="brand-name">Pet Spine and Care Center</span>
  </div>
  <svg class="footer-curve" width="405" height="45" viewBox="0 0 405 45">
    <path d="M0 8 Q200 2 405 0 L405 6 Q200 10 0 14 Z" fill="var(--sage)"/>
    <path d="M0 16 Q200 12 405 8 L405 45 L0 45 Z" fill="var(--navy)"/>
  </svg>
  <p class="return-address">4170 Larkfield Hwy Elmsbury, NH 03299</p>
</section>

<section class="sheet letterhead" aria-label="Letterhead">
  <div class="contact">
    <p>4170 Larkfield Hwy</p>
    <p>Elmsbury, NH 03299</p>
    <p class="contact-row" style="margin-top:3px">
      <svg class="icon" viewBox="0 0 10 10"><circle cx="5" cy="5" r="5" fill="var(--sage)"/><path d="M3 2.5 L4.3 2.5 L4.8 4 L4 4.6 Q4.7 6 5.6 6.2 L6.2 5.4 L7.6 6 L7.5 7.4 Q4 7.6 2.6 3.6 Z" fill="#fff"/></svg>
      508-347-6620</p>
    <p class="contact-row">
      <svg class="icon" viewBox="0 0 10 10"><circle cx="5" cy="5" r="5" fill="var(--sage)"/><rect x="2.4" y="3.2" width="5.2" height="3.6" fill="none" stroke="#fff" stroke-width=".8"/><path d="M2.4 3.2 L5 5.3 L7.6 3.2" fill="none" stroke="#fff" stroke-width=".8"/></svg>
      marisol.tedder@petspineandcare.com</p>
    <p class="contact-row">
      <svg class="icon" viewBox="0 0 10 10"><circle cx="5" cy="5" r="5" fill="var(--sage)"/><circle cx="5" cy="5" r="2.6" fill="none" stroke="#fff" stroke-width=".7"/><path d="M2.4 5 H7.6 M5 2.4 V7.6" stroke="#fff" stroke-width=".6"/></svg>
      www.petspineandcare.com</p>
  </div>
  <div class="brand">
    <span class="brand-dot"></span>
    <span class="brand-name">Pet Spine and Care Center</span>
  </div>
  <span class="fold" style="top:210px"></span>
  <span class="fold" style="top:430px"></span>
  <svg class="footer-curve" width="464" height="100" viewBox="0 0 464 100">
    <path d="M0 0 Q260 18 464 56 L464 60 Q260 22 0 6 Z" fill="var(--sage)"/>
    <path d="M0 14 Q260 30 464 62 L464 100 L0 100 Z" fill="var(--navy)"/>
  </svg>
  <p class="credentials"><strong>MARISOL TEDDER</strong> · DVM, DACVIM (Neurology) · Certified Veterinary Pain Practitioner · Certified Canine Rehabilitation Therapist</p>
</section>

</body>
</html>
```